BRIARCROFT WINE LABEL RANGE PROJECT

We need an elegant wine label design for our new range of wine. We need 3 labels for the range

2015 Briarcroft Shiraz
2015 Briarcroft Cabernet
2015 Briarcroft Shiraz Cabernet

The Size is nominated at 120mm High x 70mm Wide (Front and Back) but we are open to creative expression even if size differs

We are open to any style of label and designer can work on their strengths. it can be modern/classic/old fashion etc

I will attach the tasting notes which shows the title of wine for front label and tasting notes and details to be included at back. Please leave space for a barcode.

Thanks
Tomas.

Target Market(s)

WINE DRINKERS 35-65

Requirements
Must have
• ELEGANCE

```html
<!DOCTYPE html>
<html lang="en">
<head>
<meta charset="utf-8">
<title>Briarcroft Wine Label Range</title>
<link rel="stylesheet" href="https://fonts.googleapis.com/css2?family=Marcellus&family=Kaushan+Script&display=swap">
<style>
  :root {
    --page: #ffffff;
    --label-black: #0b0b0b;
    --ink-light: #ececec;
    --shiraz: #ea8f16;
    --shiraz-deep: #9a5a06;
    --cabernet: #c52ec4;
    --cabernet-deep: #6e0f70;
    --blend: #e0121d;
    --blend-deep: #7a0710;
  }
  * { box-sizing: border-box; margin: 0; padding: 0; }
  html, body {
    width: 1200px;
    height: 1184px;
    overflow: hidden;
    background: var(--page);
  }
  .range {
    display: flex;
    justify-content: center;
    align-items: center;
    gap: 40px;
    width: 1200px;
    height: 1184px;
  }
  .label {
    position: relative;
    width: 340px;
    height: 620px;
    background: var(--label-black);
    font-family: "Marcellus", serif;
    color: var(--ink-light);
    overflow: hidden;
  }
  .label--shiraz { --accent: var(--shiraz); --accent-deep: var(--shiraz-deep); }
  .label--cabernet { --accent: var(--cabernet); --accent-deep: var(--cabernet-deep); }
  .label--blend { --accent: var(--blend); --accent-deep: var(--blend-deep); }

  .label__band {
    position: absolute;
    top: 0; left: 0; right: 0;
    height: 92px;
    background: linear-gradient(180deg, var(--accent) 0%, var(--accent) 60%, color-mix(in srgb, var(--accent) 85%, #000) 100%);
  }
  .label__origin {
    position: absolute;
    top: 58px;
    left: 0;
    width: 272px;
    text-align: center;
    font-size: 20px;
    letter-spacing: 0.2px;
    color: var(--ink-light);
  }
  .label__vine {
    position: absolute;
    top: 36px;
    right: 0;
    width: 68px;
    bottom: 24px;
    background: linear-gradient(180deg, var(--accent) 0%, var(--accent-deep) 55%, var(--accent) 100%);
    opacity: 0.85;
  }
  .label__body {
    position: absolute;
    left: 0;
    width: 282px;
    text-align: center;
  }
  .label__vintage {
    top: 318px;
    font-size: 19px;
  }
  .label__region {
    top: 350px;
    font-family: "Kaushan Script", cursive;
    font-size: 23px;
    color: var(--accent);
  }
  .label__brand {
    top: 382px;
    font-size: 42px;
    letter-spacing: -0.5px;
    line-height: 1;
  }
  .label__variety {
    top: 432px;
    font-size: 20px;
  }
  .label__blend {
    top: 548px;
    font-size: 21px;
  }
  .label__drinks {
    top: 576px;
    font-size: 11px;
  }
</style>
</head>
<body>
<main class="range">
  <article class="label label--shiraz">
    <div class="label__band"></div>
    <p class="label__origin">WINE OF AUSTRALIA</p>
    <div class="label__vine" role="img" aria-label="Orange grapevine and leaf ornament running down the label edge"></div>
    <p class="label__body label__vintage">2015</p>
    <p class="label__body label__region">South Australian</p>
    <h2 class="label__body label__brand">BRIARCROFT</h2>
    <p class="label__body label__variety">SHIRAZ</p>
    <p class="label__body label__blend">SHIRAZ CABERNET</p>
    <p class="label__body label__drinks">STANDARD DRINKS : 8.3</p>
  </article>

  <article class="label label--cabernet">
    <div class="label__band"></div>
    <p class="label__origin">WINE OF AUSTRALIA</p>
    <div class="label__vine" role="img" aria-label="Magenta grapevine and leaf ornament running down the label edge"></div>
    <p class="label__body label__vintage">2015</p>
    <p class="label__body label__region">South Australian</p>
    <h2 class="label__body label__brand">BRIARCROFT</h2>
    <p class="label__body label__variety">CABERNET</p>
    <p class="label__body label__blend">SHIRAZ CABERNET</p>
    <p class="label__body label__drinks">STANDARD DRINKS : 8.3</p>
  </article>

  <article class="label label--blend">
    <div class="label__band"></div>
    <p class="label__origin">WINE OF AUSTRALIA</p>
    <div class="label__vine" role="img" aria-label="Red grapevine and leaf ornament running down the label edge"></div>
    <p class="label__body label__vintage">2015</p>
    <p class="label__body label__region">South Australian</p>
    <h2 class="label__body label__brand">BRIARCROFT</h2>
    <p class="label__body label__variety">SHIRAZ CABERNET</p>
    <p class="label__body label__blend">SHIRAZ CABERNET</p>
    <p class="label__body label__drinks">STANDARD DRINKS : 8.3</p>
  </article>
</main>
</body>
</html>
```